Marketing Flyer

I need a flyer for my marketing company. I would like for it to to be consistent with my logo and business card design. I would also like for there to be an image of a crowded waiting room, or restaurant with people gathered around a flat screen that reads "Your Ad Here".

• logo, info on attached doc.
• Possibly a picture people in a waiting room or restaurant with a digital sign present that reads "your ad here".

```html
<!DOCTYPE html>
<html lang="en">
<head>
<meta charset="utf-8">
<title>FieldSprout Marketing – Flyer</title>
<link rel="stylesheet" href="https://fonts.googleapis.com/css2?family=Outfit:wght@400;500;600;700;800&display=swap">
<style>
  :root {
    --backdrop: #c3cabb;
    --paper: #ffffff;
    --green: #8dc63f;
    --grey: #616161;
    --grey-dark: #555555;
    --ink: #1f1f1f;
    --screen-text: #eef3df;
    --brick-a: #9a5a48;
    --brick-b: #6b3a2e;
    --crowd: #3a2c28;
  }
  * { margin: 0; padding: 0; box-sizing: border-box; }
  html, body { width: 962px; height: 1200px; overflow: hidden; }
  body { background: var(--backdrop); font-family: "Outfit", sans-serif; position: relative; }

  .flyer {
    position: absolute; left: 45px; top: 35px; width: 873px; height: 1129px;
    background: var(--paper); box-shadow: 0 4px 14px rgba(0,0,0,.35); overflow: hidden;
  }
  .brand {
    position: absolute; left: 30px; top: 30px; display: flex; align-items: center; gap: 12px;
    font-weight: 700; font-size: 44px; color: var(--grey); letter-spacing: -0.5px;
  }
  .brand-dot { width: 22px; height: 22px; border-radius: 50%; background: var(--green); }

  .contact-title {
    position: absolute; left: 593px; width: 207px; top: 14px; text-align: center;
    font-weight: 600; font-size: 28px; color: var(--grey);
  }
  .contact-rule { position: absolute; left: 593px; top: 56px; width: 207px; height: 2px; background: var(--green); }
  .contact-pill {
    position: absolute; left: 538px; top: 69px; width: 318px; height: 54px;
    background: var(--grey); border: 3px solid var(--green); border-radius: 27px;
  }

  .hero { position: absolute; left: 0; top: 131px; width: 873px; height: 435px; overflow: hidden; }
  .hero-photo {
    position: absolute; inset: 0;
    background: linear-gradient(180deg, var(--brick-a) 0%, var(--brick-b) 60%, var(--crowd) 100%);
  }
  .ad-screen {
    position: absolute; left: 195px; top: 14px; width: 392px; height: 218px;
    background: var(--grey-dark); border: 5px solid #222;
    display: flex; align-items: flex-start; justify-content: center; padding-top: 18px;
    text-align: center; color: var(--screen-text); font-weight: 600; font-size: 58px; line-height: 0.98;
  }
  .hero-headline {
    position: absolute; left: 0; right: 0; top: 300px; text-align: center;
    color: #fff; font-weight: 800; font-size: 50px; line-height: 1.1;
    text-shadow: 0 2px 6px rgba(0,0,0,.5);
  }

  .benefits-title {
    position: absolute; left: 0; right: 0; top: 583px; text-align: center;
    color: var(--green); font-weight: 600; font-size: 39px;
  }
  .benefits-rule { position: absolute; left: 23px; top: 641px; width: 820px; height: 3px; background: var(--green); }

  .what-tab {
    position: absolute; left: 0; top: 667px; width: 262px; height: 48px;
    background: var(--grey); clip-path: polygon(0 0, 100% 0, 94% 100%, 0 100%);
    color: var(--green); font-weight: 700; font-size: 27px; line-height: 48px; padding-left: 38px;
  }
  .what-text {
    position: absolute; left: 291px; top: 658px; width: 560px;
    color: var(--grey); font-weight: 500; font-size: 27px; line-height: 34px;
  }

  .benefit-list { list-style: none; }
  .benefit {
    position: absolute; left: 72px; width: 790px;
    font-size: 18px; line-height: 26px; color: var(--ink);
  }
  .benefit svg { position: absolute; left: -44px; top: 0; width: 28px; height: 28px; }

  .footer-band { position: absolute; left: 0; bottom: 0; width: 873px; height: 24px; background: var(--green); }
</style>
</head>
<body>
<main class="flyer">
  <header>
    <div class="brand"><span class="brand-dot"></span>FieldSprout Marketing</div>
    <div class="contact-title">Contact</div>
    <div class="contact-rule"></div>
    <div class="contact-pill"></div>
  </header>

  <section class="hero">
    <div class="hero-photo" role="img" aria-label="Photo of a crowded sports bar with a brick wall, wall-mounted TVs showing a football match and fans cheering"></div>
    <div class="ad-screen">YOUR AD<br>HERE</div>
    <h1 class="hero-headline">Let us make you famous<br>in your community!</h1>
  </section>

  <h2 class="benefits-title">Benefits of Advertising with FieldSprout</h2>
  <div class="benefits-rule"></div>

  <div class="what-tab">WHAT WE DO</div>
  <p class="what-text">We design an ad for your company and place it on the TV at local businesses.</p>

  <ul class="benefit-list">
    <li class="benefit" style="top:741px">
      <svg viewBox="0 0 28 28"><circle cx="14" cy="14" r="13" fill="#8dc63f"/><text x="14" y="19.5" text-anchor="middle" font-family="Outfit, sans-serif" font-weight="700" font-size="16" fill="#fff">$</text></svg>
      Inexpensive: Only $31.00 per month!
    </li>
    <li class="benefit" style="top:777px">
      <svg viewBox="0 0 28 28"><rect x="2" y="4" width="24" height="16" rx="2" fill="#8dc63f"/><polyline points="6,16 11,11 15,14 22,8" fill="none" stroke="#fff" stroke-width="2"/><rect x="10" y="22" width="8" height="2" fill="#8dc63f"/></svg>
      Exposure: Our digital signage is placed in only the<br>best/high traffic businesses in your area.
    </li>
    <li class="benefit" style="top:839px">
      <svg viewBox="0 0 28 28"><circle cx="14" cy="14" r="13" fill="#8dc63f"/><path d="M8 14a6 6 0 0 1 10.5-4M20 14a6 6 0 0 1-10.5 4" fill="none" stroke="#fff" stroke-width="2.2"/><path d="M19.5 6v4.5h-4.5M8.5 22v-4.5h4.5" fill="none" stroke="#fff" stroke-width="2"/></svg>
      Repetition: Your ad is shown over 3,500 time each month (42,000 times per year)!
    </li>
    <li class="benefit" style="top:877px">
      <svg viewBox="0 0 28 28"><path d="M14 1a5 5 0 0 1 5 5c0 4-5 8-5 8s-5-4-5-8a5 5 0 0 1 5-5z" fill="#8dc63f"/><circle cx="14" cy="6" r="2" fill="#fff"/><circle cx="7" cy="18" r="3" fill="#8dc63f"/><circle cx="21" cy="18" r="3" fill="#8dc63f"/><rect x="3" y="22" width="22" height="5" rx="2.5" fill="#8dc63f"/></svg>
      Local: We show your ad to consumers in YOUR area. Let us help you do business<br>with the people you want to do business with.
    </li>
    <li class="benefit" style="top:934px">
      <svg viewBox="0 0 28 28"><circle cx="14" cy="14" r="13" fill="#8dc63f"/><polygon points="14,6 16.4,11.3 22,11.8 17.7,15.4 19,21 14,18 9,21 10.3,15.4 6,11.8 11.6,11.3" fill="#fff"/></svg>
      Exclusivity: Only 2 ads per industry.
    </li>
    <li class="benefit" style="top:973px">
      <svg viewBox="0 0 28 28"><circle cx="14" cy="6" r="3.5" fill="#8dc63f"/><rect x="10" y="11" width="8" height="14" rx="3" fill="#8dc63f"/><circle cx="5" cy="9" r="2.8" fill="#8dc63f"/><rect x="2" y="13" width="6" height="11" rx="2.5" fill="#8dc63f"/><circle cx="23" cy="9" r="2.8" fill="#8dc63f"/><rect x="20" y="13" width="6" height="11" rx="2.5" fill="#8dc63f"/></svg>
      Lead Generation: We show consumers how to reach you and where to find you.
    </li>
    <li class="benefit" style="top:1007px">
      <svg viewBox="0 0 28 28"><path d="M14 2a9 9 0 0 1 5 16.5V22H9v-3.5A9 9 0 0 1 14 2z" fill="#8dc63f"/><rect x="10" y="23" width="8" height="3" rx="1.5" fill="#8dc63f"/><path d="M14 7v7" stroke="#fff" stroke-width="2"/></svg>
      Brand Awareness: People need to know your business. We make that happen<br>by putting your brand right in front of them.
    </li>
    <li class="benefit" style="top:1067px">
      <svg viewBox="0 0 28 28"><circle cx="14" cy="14" r="13" fill="#8dc63f"/><path d="M7 12h4l7-4v12l-7-4H7z" fill="#fff"/><rect x="9" y="16" width="2.5" height="5" fill="#fff"/></svg>
      Digital: Digital advertising has higher retention rates and higher consumer engagement.
    </li>
  </ul>

  <div class="footer-band"></div>
</main>
</body>
</html>
```